Banner ad design for Vantor Reach Ads

We are looking for a designer to develop a concept for banner ads for a Vantor Reach campaign we are building.

We have 3 business lines, shredding services, records management services and scanning services.

We are looking for 4 sets of ads to be created, one for each business line + one set that showcases all of our lines together.

For the design concepts, we would like to see a few sizes (banner, square, leaderboard, skyscraper, etc) for each.

The person chosen will then need to create the ads into all Vantor supported sizes -- 20 sizes total for each set of ads as per the Vantor size guidelines found on this page - https://help.vantor.example/vantor-ads/answer/4859210?hl=en&ref_topic=6082714#

A few items to note:
- Design should complement our existing brand/website look and feel (www.gold-kettle.ca)
- Each final ad must be 150Kb or less in size
- Final designs should be editable, meaning if we would like to change some copy in the design, we can do so using a well-known software (Canva, Photoshop/InDesign, etc)
- Some images are attached for use, but if you feel a different stock image is more suitable to to your design, please go ahead and use it.

Provided below is some messaging that can be used for each set of ads. Do not feel you need to use all of the messaging, it is provided for guidance.

SHREDDING SERVICES:

Possible Short Headline:
-- One-Time Shredding Services
-- Secure Shredding Services
-- Affordable On-Site Shredding

Possible Long Headline
-- Your Paper Can be Destroyed as Soon as the Next Business Day

Possible Descriptions:
-- QVRB AAA Certified On site shredding company. Service as soon as Next Day.
-- Secure and Affordable Toronto & GTA On-Site Shredding.
-- Certified, Affordable Office Shredding Since 2003.
-- Quick, no contact and affordable paper shredding services in Toronto & Southern Ontario.
-- Certified, Affordable Office Shredding Since 2003. Fast, no contact shredding service.

Call to Action
-- Get a Quote

RECORDS MANAGEMENT
Short Headline:
-- Off-site Records Storage
-- Records Management & Storage
-- Secure Records Storage
-- Records Management Services
-- Long Term Records Management
-- Document Storage Solutions

Possible Description
-- Local, Affordable Storage Solutions. Protect and Store your Documents in our Secure Facility
-- Local, Affordable Records Management Solutions. Store your Records in our Secure Facility
-- Certified, Affordable Document Storage Since 2004. Contact Us for a Free Quote!
-- Vaultmark+ Certified, Affordable Document Storage Since 2004. Contact Us for a Free Quote!

Call to Action
-- Get a Quote

SCANNING SERVICES

Short Headline:
-- Professional Scanning Company
-- Toronto & GTA Scanning Service
-- Document Scanning Services
-- Digital Conversion Services
-- Fast & Easy Retrieval

Description
-- Scan and documents and files with Professional scanning services from Gold-Kettle
-- Convert Your Paper Files to Electronic Files. Fast & Easy Retrieval.
-- Easily access your documents electronically with Document Scanning Services

Call to Action
-- Get a Quote

ALL SERVICES AD SET
Short Headline
-- Shred, Scan & Store Documents
-- Secure Shredding, Records Management and Scanning Services
-- #1 Document Management Company
-- Gold Kettle Shredding, Storage & Scanning

Description
-- Secure and Affordable Toronto & GTA On-Site Shredding, Document Storage & Scanning Company

Call to Action
-- Get a Quote

Font styles to use
Sans Serif

```html
<!DOCTYPE html>
<html lang="en">
<head>
<meta charset="utf-8">
<title>Vantor Reach Ads – Gold-Kettle Banner Concepts</title>
<link href="https://fonts.googleapis.com/css2?family=Montserrat:wght@400;500;600&display=swap" rel="stylesheet">
<style>
  :root {
    --brand-blue: #0b9ddf;
    --brand-light: #6ec9ef;
    --brand-pale: #b7e3f6;
    --ink: #1c1c1c;
    --paper: #ffffff;
    --canvas: #ffffff;
    --photo-office: #8f8a82;
    --photo-files: #8a8580;
    --photo-dark: #3b3b3d;
  }
  * { box-sizing: border-box; margin: 0; padding: 0; }
  html, body { width: 1043px; height: 1200px; overflow: hidden; background: var(--canvas); }
  body { position: relative; font-family: "Montserrat", Arial, sans-serif; color: var(--ink); }

  .ad { position: absolute; overflow: hidden; background: var(--paper);
        box-shadow: 0 2px 8px rgba(0,0,0,0.12); }
  .ad--square { width: 335px; height: 230px; left: 60px; }
  .ad--leader { width: 537px; height: 104px; left: 447px; }
  .row-1 { top: 63px; } .row-2 { top: 345px; } .row-3 { top: 626px; } .row-4 { top: 906px; }

  .ad svg.art { position: absolute; left: 0; top: 0; }
  .copy { position: absolute; }
  .headline { font-weight: 500; text-transform: uppercase; letter-spacing: 0.03em; line-height: 1.12; }
  .headline--square { font-size: 20px; }
  .headline--leader { font-size: 14px; }
  .lede { font-size: 8.6px; line-height: 1.5; margin-top: 6px; }
  .promise { color: var(--brand-blue); font-size: 10.6px; line-height: 1.1; margin-top: 6px; }
  .cta { display: inline-block; margin-top: 12px; width: 83px; height: 23px; line-height: 23px;
         text-align: center; font-size: 9.4px; font-weight: 600; border-radius: 2px;
         background: var(--brand-blue); color: var(--paper); letter-spacing: 0.02em; }
  .cta--light { background: var(--paper); color: var(--brand-blue); }
  .center { text-align: center; color: var(--paper); }
</style>
</head>
<body>

<!-- Shredding square -->
<section class="ad ad--square row-1">
  <svg class="art" width="335" height="230" viewBox="0 0 335 230">
    <path d="M70 0 H146 Q95 60 135 120 Q160 180 130 230 H160 Q200 150 170 90 Q145 40 146 0 Z" fill="var(--brand-pale)"/>
    <path d="M0 0 H110 Q70 40 110 110 Q150 170 130 230 H0 Z" fill="var(--brand-light)"/>
    <path d="M0 0 H90 Q150 30 158 115 Q162 190 130 230 H0 Z" fill="var(--photo-office)" role="img" aria-label="Photo of a woman feeding papers into a shredding bin in an office"/>
  </svg>
  <div class="copy" style="left:173px; top:26px; width:155px;">
    <h2 class="headline headline--square">One-Time<br>Shredding<br>Services</h2>
    <p class="lede">Your Paper Can be Destroyed as Soon as the Next Business Day</p>
    <p class="promise">QVRB AAA Certified On site shredding company.<br>Service as soon as Next Day.</p>
    <span class="cta">Get a Quote</span>
  </div>
</section>

<!-- Shredding leaderboard -->
<section class="ad ad--leader row-1">
  <svg class="art" width="537" height="104" viewBox="0 0 537 104">
    <path d="M170 0 H247 Q225 50 247 104 H170 Q205 52 170 0 Z" fill="var(--brand-light)"/>
    <path d="M0 0 H186 Q160 52 186 104 H0 Z" fill="var(--photo-office)" role="img" aria-label="Photo of a woman using a shredding bin in an office cubicle"/>
    <path d="M186 30 L206 52 L186 75 Q176 52 186 30 Z" fill="var(--brand-blue)"/>
  </svg>
  <div class="copy" style="left:258px; top:6px; width:275px;">
    <h2 class="headline headline--leader">One-Time Shredding Services</h2>
    <p class="lede" style="margin-top:3px;">Your Paper Can be Destroyed as Soon as the Next Business Day</p>
    <p class="promise" style="margin-top:7px;">QVRB AAA Certified On site shredding company.<br>Service as soon as Next Day.</p>
    <span class="cta" style="margin-top:8px;">Get a Quote</span>
  </div>
</section>

<!-- Storage square -->
<section class="ad ad--square row-2">
  <svg class="art" width="335" height="230" viewBox="0 0 335 230">
    <path d="M0 0 H215 L222 36 L176 84 L176 100 L110 176 L0 196 Z" fill="var(--photo-files)" role="img" aria-label="Photo of hands pulling colourful file folders from a cabinet"/>
    <g stroke="var(--paper)" stroke-width="4" fill="none">
      <line x1="86" y1="0" x2="178" y2="92"/>
      <line x1="0" y1="100" x2="104" y2="-4"/>
      <line x1="0" y1="150" x2="60" y2="90"/>
    </g>
    <path d="M93 0 H139 L116 22 Z" fill="var(--brand-blue)"/>
    <path d="M25 172 L58 139 L91 172 L58 205 Z" fill="var(--brand-blue)"/>
  </svg>
  <div class="copy" style="left:179px; top:84px; width:155px;">
    <h2 class="headline headline--square">Off-Site<br>Records<br>Storage</h2>
    <p class="lede" style="margin-top:5px;">Local, Affordable Storage Solutions. Protect and Store your Documents in our Secure Facility</p>
    <span class="cta" style="margin-top:8px;">Get a Quote</span>
  </div>
</section>

<!-- Storage leaderboard -->
<section class="ad ad--leader row-2">
  <svg class="art" width="537" height="104" viewBox="0 0 537 104">
    <g role="img" aria-label="Photo of an office cluttered with stacks of paper files">
      <path d="M0 0 H108 L50 104 H32 Z" fill="#8b8d8f"/>
      <path d="M118 0 L62 104 H170 Z" fill="#7a7068"/>
      <path d="M126 0 H255 L195 104 H184 Z" fill="#9a8a6e"/>
    </g>
  </svg>
  <div class="copy" style="left:269px; top:12px; width:264px;">
    <h2 class="headline headline--leader">Off-Site Records Storage</h2>
    <p class="lede" style="margin-top:7px;">Local, Affordable Storage Solutions. Protect and Store your Documents in our Secure Facility</p>
    <span class="cta" style="margin-top:8px;">Get a Quote</span>
  </div>
</section>

<!-- Scanning square -->
<section class="ad ad--square row-3">
  <svg class="art" width="335" height="230" viewBox="0 0 335 230">
    <rect width="335" height="230" fill="#9a9a96" role="img" aria-label="Photo of a technician loading documents into a scanner"/>
    <path d="M0 0 H155 L335 175 V230 H200 L0 60 Z" fill="var(--brand-light)" opacity="0.9"/>
    <path d="M0 60 L200 230 H150 L0 110 Z" fill="var(--brand-blue)" opacity="0.75"/>
  </svg>
  <div class="copy center" style="left:0; top:56px; width:335px;">
    <h2 class="headline" style="font-size:17px; line-height:1.2;">Professional Scanning<br>Company</h2>
    <p class="lede" style="font-size:10.4px; margin-top:10px;">Scan and documents and files with Professional scanning<br>services from Gold-Kettle</p>
    <span class="cta cta--light" style="margin-top:12px;">Get a Quote</span>
  </div>
</section>

<!-- Scanning leaderboard -->
<section class="ad ad--leader row-3">
  <svg class="art" width="537" height="104" viewBox="0 0 537 104">
    <path d="M284 104 V55 H304" fill="none" stroke="var(--brand-blue)" stroke-width="1.2"/>
    <rect x="297" y="70" width="6" height="34" fill="var(--brand-blue)"/>
    <rect x="303" y="0" width="234" height="104" fill="#b8a978" role="img" aria-label="Photo of a worker at a desk among shelves of boxes and stacked files"/>
  </svg>
  <div class="copy" style="left:8px; top:12px; width:290px;">
    <h2 class="headline headline--leader">Professional Scanning Company</h2>
    <p class="lede" style="margin-top:7px;">Scan and documents and files with Professional scanning services from Gold-Kettle</p>
    <span class="cta" style="margin-top:8px;">Get a Quote</span>
  </div>
</section>

<!-- All services square -->
<section class="ad ad--square row-4">
  <svg class="art" width="335" height="230" viewBox="0 0 335 230">
    <rect width="335" height="230" fill="#5a5a6e" role="img" aria-label="Photo of a warehouse aisle with tall shelving full of archive boxes"/>
    <path d="M112 4 L220 112 L112 228 L0 115 V108 Z" fill="var(--brand-blue)" opacity="0.93"/>
  </svg>
  <div class="copy center" style="left:0; top:58px; width:224px;">
    <h2 class="headline" style="font-size:13px; line-height:1.25;">Shred, Scan<br>&amp;<br>Store Documents</h2>
    <p class="lede" style="margin-top:7px;">Secure and Affordable Toronto &amp; GTA<br>On-Site Shredding, Document Storage<br>&amp; Scanning Company</p>
    <span class="cta cta--light" style="margin-top:10px;">Get a Quote</span>
  </div>
</section>

<!-- All services leaderboard -->
<section class="ad ad--leader row-4">
  <svg class="art" width="537" height="104" viewBox="0 0 537 104">
    <rect width="537" height="104" fill="var(--photo-dark)" role="img" aria-label="Darkened photo of a technician carrying a document box"/>
  </svg>
  <div class="copy center" style="left:0; top:10px; width:537px;">
    <h2 class="headline headline--leader" style="font-size:15px;">Shred, Scan &amp; Store Documents</h2>
    <p class="lede" style="margin-top:4px;">Secure and Affordable Toronto &amp; GTA On-Site Shredding, Document Storage<br>&amp; Scanning Company</p>
    <span class="cta" style="margin-top:5px;">Get a Quote</span>
  </div>
</section>

</body>
</html>
```